Birchwell Entreprise Campus Media Package

We are looking for a designer to unify our company's image throughout its stationery and marketing deliverables. We will be focusing on:
*Business Cards (3.5 x 2)
*Letter Head (Letter Size)
*PowerPoint Presentation Template,
*One Pager Flyer (Letter Size)
*Front of Elevator's bay: 4 photos of the elevator bays (two groups of 3 elevators) to which we are looking for designs for its doors and surrounding wall (vinyl prints)
*Font's suggestions
*Official color palette.
*Outdoor Street Signage: please use the following dimensions:
Sign #1 (Richmond Side): 48(W)x72"(H) (3 sided)
Sign #2: 24"(W)x48"(H) (3 sided)
Sign #3 (Top of Hill): 30(W)x54(H) (2 sides)
*Carport Sign:
See photos attached. The white letters will be removed, and a new sign will take place. Preferably, Cut-Out fonts, but we can consider an alternative approach for cost effective solution.
Find attached the approved logos.
______________________________________
We are a real estate holding company focused on the commercial office space in the Ohio, US, market.
You can check our site at www.birchwellcampus-example.com
As inspiration guidelines, we would like to see designs that are modern, minimalistic, dynamic and energetic.
Updates
Target Market(s)
General Population, Business Owners, Non-Profit Organizations, Government
Industry/Entity Type
Real Estate - Commercial Office Space - Flex Space
Look and feel
Each slider illustrates characteristics of the customer's brand and the style your logo design should communicate.

```html
<!DOCTYPE html>
<html lang="en">
<head>
<meta charset="utf-8">
<title>Birchwell Entreprise Campus – Business Card</title>
<link href="https://fonts.googleapis.com/css2?family=Open+Sans:wght@400;600;700&display=swap" rel="stylesheet">
<style>
  :root {
    --brand-blue: #1380c4;
    --ink: #1f1f1f;
    --paper: #ffffff;
    --backdrop: #e9ebee;
  }
  * { margin: 0; padding: 0; box-sizing: border-box; }
  html, body { width: 1200px; height: 900px; overflow: hidden; }
  body {
    background: var(--backdrop);
    font-family: "Open Sans", Arial, sans-serif;
    position: relative;
  }
  .card {
    position: absolute;
    left: 330px;
    width: 540px;
    height: 348px;
    box-shadow: 0 2px 8px rgba(0,0,0,0.12);
  }
  .card--front { top: 80px; background: var(--paper); }
  .card--back { top: 484px; background: var(--brand-blue); }

  .side-bar {
    position: absolute;
    top: 87px;
    width: 19px;
    height: 174px;
    background: var(--brand-blue);
  }
  .side-bar--left { left: 0; }
  .side-bar--right { right: 0; }

  .wordmark {
    position: absolute;
    display: flex;
    align-items: center;
    gap: 12px;
    font-weight: 600;
    white-space: nowrap;
  }
  .wordmark__dot {
    width: 22px; height: 22px;
    border-radius: 50%;
    flex: none;
  }
  .card--front .wordmark {
    left: 0; right: 0; top: 150px;
    justify-content: center;
    color: var(--ink);
    font-size: 24px;
  }
  .card--front .wordmark__dot { background: var(--brand-blue); }
  .card--back .wordmark {
    left: 0; right: 0; top: 158px;
    justify-content: center;
    color: var(--paper);
    font-size: 26px;
  }
  .card--back .wordmark__dot { background: var(--paper); }

  .contact {
    position: absolute;
    top: 245px;
    left: 0; right: 0;
    display: flex;
    justify-content: center;
  }
  .contact__col { padding: 0 10px; }
  .contact__col--person {
    text-align: right;
    border-right: 1.5px solid var(--brand-blue);
  }
  .contact__heading {
    color: var(--brand-blue);
    font-weight: 600;
    font-size: 16px;
    line-height: 18px;
    text-transform: uppercase;
  }
  .contact__sub {
    color: var(--ink);
    font-weight: 700;
    font-size: 9.5px;
    line-height: 13px;
    margin-bottom: 14px;
    letter-spacing: 0.3px;
  }
  .contact__line {
    color: var(--ink);
    font-size: 9px;
    line-height: 15px;
  }
</style>
</head>
<body>
  <section class="card card--front">
    <div class="side-bar side-bar--left"></div>
    <div class="side-bar side-bar--right"></div>

    <div class="wordmark">
      <span class="wordmark__dot"></span>
      <span class="wordmark__name">Birchwell Entreprise Campus</span>
    </div>

    <div class="contact">
      <div class="contact__col contact__col--person">
        <p class="contact__heading">Daniel Marsh</p>
        <p class="contact__sub">GENERAL MANAGER</p>
        <p class="contact__line">www.birchwellcampus-example.com</p>
        <p class="contact__line">dmarsh@birchwellcampus-example.com</p>
      </div>
      <div class="contact__col contact__col--office">
        <p class="contact__heading">Office Adress</p>
        <p class="contact__sub">4180 Harbor Lane Avon OH 44011</p>
        <p class="contact__line">Phone 440-555-0143</p>
        <p class="contact__line">Fax 440-555-0143</p>
      </div>
    </div>
  </section>

  <section class="card card--back">
    <div class="wordmark">
      <span class="wordmark__dot"></span>
      <span class="wordmark__name">Birchwell Entreprise Campus</span>
    </div>
  </section>
</body>
</html>
```